Dog Snacks brand needs a new packaging design

Dear Designers,

We are looking for a packaging expert to design our new line of Dog Snacks which contain a relaxing hemp extract (CBD).

Our company is already selling various relaxing cat & dog products , and we would like this new design to reflect the same "style & feeling" as our current products (see attached instructions).

Technical aspects:
- The packaging is a Stand Up Pouch (12x18.5x7cm - see attached instructions).
- Please follow technical guidelines from printer (see attached instructions).
- The packaging will contain 120g of high-quality, semi-moist dog snacks.
- We will be designing 3 differents variations for 3 different flavours: Chicken, Beef & Liver.
- The packaging will be printed with a matt finish.

Design aspects:
- The design should be compatible with our brand identity (i.e. fluffly, pure, relaxing, positive, clean & natural).
- Soft/rounded shapes are preferred.
- Please use our brand's colors (#3BA384, White & Black).
- Please use our company logo (see attached instructions).
- The design also needs to convey a strong sense of professionalism as we are an animal "healthcare" brand.
- If you want to include a dog picture, we would prefer you to use a picture of our official brand ambassador (see attached instructions).
- We have attached a number of packaging examples which we like a lot. (see attached instructions). Please only use those as general inspiration.
- Only original work (no plagiarism will be accepted).

Please don't hesitate to send us a message if you have any questions about the brand, the product or the design requirements.

We look forward to seeing your designs & working on this together !

Thanks & regards,
Marcus

Dog owners

Pet Care

Sans Serif

• Please see project description.

```html
<!DOCTYPE html>
<html lang="en">
<head>
<meta charset="utf-8">
<title>Verdalis CalmBites CBD Treats – Chicken pouch</title>
<link rel="stylesheet" href="https://fonts.googleapis.com/css2?family=Arvo:wght@400;700&family=Lexend:wght@400;500&display=swap">
<style>
  :root {
    --backdrop: #1d2f29;
    --brand-green: #1f7a5c;
    --brand-green-light: #3ba384;
    --ink: #1b1f1d;
    --foil-light: #f4f5f5;
    --foil-mid: #dcdfdf;
    --foil-dark: #c3c7c7;
    --white: #ffffff;
  }
  * { margin: 0; padding: 0; box-sizing: border-box; }
  html, body { width: 1200px; height: 960px; overflow: hidden; }
  body {
    background: var(--backdrop);
    font-family: "Lexend", sans-serif;
    position: relative;
  }
  .pouch {
    position: absolute;
    left: 362px; top: 103px;
    width: 476px; height: 762px;
    border-radius: 22px 22px 6px 6px;
    background: linear-gradient(90deg, var(--foil-dark) 0%, var(--foil-light) 30%, var(--white) 50%, var(--foil-light) 70%, var(--foil-mid) 100%);
    overflow: hidden;
  }
  .zip-seal {
    position: absolute; left: 0; right: 0; top: 128px;
    height: 2px; background: rgba(0,0,0,0.08);
  }
  .brand-mark {
    position: absolute; left: 50%; top: 178px;
    width: 56px; height: 56px; margin-left: -28px;
    border: 4px solid var(--brand-green); border-radius: 50%;
  }
  .brand-name {
    position: absolute; left: 0; right: 0; top: 254px;
    text-align: center;
    font-family: "Arvo", serif; font-weight: 400;
    font-size: 50px; letter-spacing: 1px; color: var(--ink);
  }
  .brand-tagline {
    position: absolute; right: 86px; top: 318px;
    font-family: "Arvo", serif; font-size: 20px; color: var(--brand-green);
  }
  .product-name {
    position: absolute; left: 0; right: 0; top: 352px;
    text-align: center; font-size: 34px; font-weight: 500;
    font-variant: small-caps; letter-spacing: 2px; color: var(--brand-green);
  }
  .product-name sup { font-size: 14px; }
  .product-type {
    position: absolute; left: 0; right: 0; top: 390px;
    text-align: center; font-size: 30px; font-weight: 500;
    letter-spacing: 2px; color: var(--ink);
  }
  .dosage-pill {
    position: absolute; left: 50%; top: 434px; transform: translateX(-50%);
    padding: 3px 12px; border-radius: 4px;
    background: linear-gradient(90deg, var(--brand-green), var(--brand-green-light));
    color: var(--white); font-size: 16px; letter-spacing: 1.5px; white-space: nowrap;
  }
  .benefits {
    position: absolute; left: 0; right: 0; top: 473px;
    text-align: center; font-size: 14px; letter-spacing: 1.5px; color: var(--ink);
  }
  .ambassador-photo {
    position: absolute; left: 194px; top: 515px;
    width: 282px; height: 197px;
    background: radial-gradient(ellipse at 55% 55%, #e7e2df 0%, #cfc9c6 45%, rgba(255,255,255,0) 75%);
  }
  .flavour-badge {
    position: absolute; left: 47px; top: 562px;
    width: 106px; height: 106px; border-radius: 50%;
    background: var(--brand-green);
    display: flex; flex-direction: column; align-items: center; justify-content: flex-end;
    padding-bottom: 20px; color: #e6f2ed;
  }
  .flavour-badge::before {
    content: ""; position: absolute; inset: 5px;
    border: 1px dashed rgba(255,255,255,0.6); border-radius: 50%;
  }
  .flavour-name { font-size: 13px; font-weight: 500; letter-spacing: 1px; border-bottom: 1px solid #e6f2ed; padding-bottom: 2px; }
  .net-weight { font-size: 11px; margin-top: 3px; letter-spacing: 1px; }
  .endorsement {
    position: absolute; left: 40px; top: 685px;
    font-size: 7.5px; line-height: 1.1; letter-spacing: 0.8px; color: var(--ink);
  }
  .endorsement strong { font-weight: 500; }
  .base-band {
    position: absolute; left: 0; right: 0; bottom: 0; height: 52px;
    background: var(--brand-green-light);
  }
</style>
</head>
<body>
  <main class="pouch">
    <div class="zip-seal"></div>
    <div class="brand-mark"></div>
    <div class="brand-name">VERDALIS</div>
    <div class="brand-tagline">For Animals</div>
    <h1 class="product-name">CalmBites<sup>™</sup></h1>
    <div class="product-type">CBD TREATS</div>
    <div class="dosage-pill">CBD 250mg | 0% THC</div>
    <div class="benefits">SUPPORT | CALM | EASE</div>
    <div class="ambassador-photo" role="img" aria-label="Photo of the brand ambassador dog, a cream shar-pei puppy wearing pink heart glasses, resting on a white rug"></div>
    <div class="flavour-badge">
      <span class="flavour-name">CHICKEN</span>
      <span class="net-weight">120G</span>
    </div>
    <p class="endorsement">RECOMMENDED BY<br><strong>VETERINARIANS</strong></p>
    <div class="base-band"></div>
  </main>
</body>
</html>
```